Thornbeck Advisory Group Business Card Design Project

2-sided business card for my small (me and a couple subcontractors) firm, which consults to public community colleges and school districts and public agencies in California on energy matters, mostly solar electric systems that can reduce their electricity use by as much as 80%. I prepare requests for proposals (RFPs), manage the RFP processes, and work with the solar vendors to get the best deal for my clients. I also do regulatory and legislative advocacy for strong renewable energy policies. I do lots of quantitative analysis to make sure the solar systems are sized to produce the maximum monetary savings and focus a lot on the aesthetic design of the solar systems, as architectural features of the campuses (most are carport structures built in parking lots, but some are built on the ground and on rooftops). All my work is geared to getting the best value, highest quality, and most reliable solar system. My career background is in public interest energy advocacy; I'm not a consultant trying to make a million dollars but someone who is still serving in the public interest.

My competition is made up of much larger firms; this business card/logo in large part is intended to present an image of my firm as an equal to these larger firms despite my smaller size.

Essential information as follows:
Firm name: Thornbeck Advisory Group
Tagline: Clean Energy Procurement for the Public Sector
Name: Walter Pennick
email, 2 phone number, and address listed as well.

Target Market(s)

Public schools, community colleges, & public agencies.There is a wide range in the sophistication of these organizations.

Industry/Entity Type

Parking

Requirements
Must have
• - several rich colors, which can be either in the logo or in the background - the overall feeling of the card should reflect richness of color. I have uploaded some photos showing some colors that I like together. By rich I do not necessarily mean bright. I suppose bright colors in the logo could be supported with rich colors in the overall background of the card.
- professional, and powerful in an understated way (not kooky, cartoonish, or very playful)
- the logo must NOT be too representational of solar energy or the sun, but at the same time it would be good for the logo to be somewhat suggestive of this.

Nice to have
• -I like abstract and geometric images (with rich colts).
- A very subtle reference to schools/colleges/education would be great but it CANNOT be explicit; it would have to be faintly suggestive.
- In the logo I like the idea of abstract or geometric shapes intersecting with other in an interesting and suggestive way, conveying the multiple aspects of my practice (economics, data analysis, energy analysis, problem solving, managing collaborative processes, policy analysis)
- My work relates to environmental concerns, especially climate change. Working this into the logo in a subtle way could be good, but it's not a requirement.
- I like the idea that the logo/card feels serene.
- In designing the business card, I kind of like the idea of having the tag line as the first thing they read, then they see the firm name.

Should not have
• Not:
- humorous
- boring
- overly slick
- overly formal
- whimsical

```html
<!DOCTYPE html>
<html lang="en">
<head>
<meta charset="utf-8">
<title>Thornbeck Advisory Group — Business Card</title>
<link href="https://fonts.googleapis.com/css2?family=Comfortaa:wght@400&family=Raleway:wght@700&display=swap" rel="stylesheet">
<style>
  :root {
    --paper: #ffffff;
    --slate-dark: #3b3b3d;
    --slate-light: #6a6a6c;
    --sky: #1ea6e2;
    --sky-deep: #0d8fd0;
    --sky-glow: #48bdf0;
    --sun: #fbc43d;
    --band-grey: #58595b;
    --ink-light: #ffffff;
  }
  * { margin: 0; padding: 0; box-sizing: border-box; }
  html, body {
    width: 1200px; height: 484px; overflow: hidden;
    background: var(--paper);
  }
  .canvas { position: relative; width: 1200px; height: 484px; }

  .card { position: absolute; top: 73px; width: 536px; height: 312px; overflow: hidden; }

  /* Shared brand block: square above, name below */
  .brand {
    position: absolute; display: flex; flex-direction: column; align-items: flex-start;
    font-family: "Comfortaa", sans-serif; font-weight: 400; color: var(--ink-light);
  }
  .brand__square { display: block; flex: none; background: var(--sun); }
  .brand__name { line-height: 1; text-transform: uppercase; white-space: nowrap; }
  .brand__name span { display: block; }

  /* Front */
  .card--front {
    left: 40px;
    background: linear-gradient(160deg, var(--slate-dark) 0%, #454547 45%, var(--slate-light) 100%);
  }
  .card--front .brand { left: 46px; top: 54px; gap: 36px; }
  .card--front .brand__square { width: 120px; height: 120px; }
  .card--front .brand__name { font-size: 34px; }
  .card--front .brand__name span + span { font-size: 12px; margin-top: 6px; letter-spacing: 0.3px; }

  .tagline {
    position: absolute; left: 268px; top: 134px; width: 268px; height: 57px;
    background: var(--sky); padding: 11px 0 0 8px;
    font-family: "Raleway", sans-serif; font-weight: 700; font-size: 14px;
    line-height: 19px; color: var(--ink-light); text-transform: uppercase;
  }

  /* Back */
  .card--back {
    left: 613px;
    background: radial-gradient(ellipse at 30% 45%, var(--sky-glow) 0%, var(--sky) 45%, var(--sky-deep) 100%);
    border-bottom: 7px solid var(--sun);
  }
  .card--back .brand { left: 52px; top: 74px; gap: 28px; }
  .card--back .brand__square { width: 100px; height: 100px; }
  .card--back .brand__name { font-size: 27px; }
  .card--back .brand__name span + span { font-size: 10px; margin-top: 5px; letter-spacing: 0.3px; }

  .person {
    position: absolute; left: 254px; top: 76px; width: 282px; height: 47px;
    background: var(--band-grey); padding-left: 10px;
    font-family: "Comfortaa", sans-serif; font-weight: 400; font-size: 31px; line-height: 47px;
    color: var(--ink-light); white-space: nowrap;
  }
  .contacts { position: absolute; left: 267px; top: 140px; list-style: none; }
  .contact {
    display: flex; align-items: center; gap: 10px; height: 24px; margin-bottom: 11px;
    font-family: "Comfortaa", sans-serif; font-weight: 400; font-size: 20px; color: var(--ink-light);
  }
  .contact__icon { width: 24px; height: 24px; flex: none; }
</style>
</head>
<body>
<main class="canvas">

  <section class="card card--front" aria-label="Card front">
    <div class="brand">
      <span class="brand__square" aria-hidden="true"></span>
      <p class="brand__name"><span>Thornbeck</span><span>Advisory Group</span></p>
    </div>
    <p class="tagline">Clean Energy Procurement<br>for the Public Sector</p>
  </section>

  <section class="card card--back" aria-label="Card back">
    <div class="brand">
      <span class="brand__square" aria-hidden="true"></span>
      <p class="brand__name"><span>Thornbeck</span><span>Advisory Group</span></p>
    </div>

    <h1 class="person">Walter Pennick</h1>

    <ul class="contacts">
      <li class="contact">
        <svg class="contact__icon" viewBox="0 0 24 24" aria-hidden="true">
          <rect width="24" height="24" rx="4" fill="var(--sun)"/>
          <rect x="8" y="4" width="8" height="16" rx="1.5" fill="none" stroke="#fff" stroke-width="1.6"/>
          <circle cx="12" cy="17" r="0.9" fill="#fff"/>
        </svg>
        <span>+ 1916 555 0142</span>
      </li>
      <li class="contact">
        <svg class="contact__icon" viewBox="0 0 24 24" aria-hidden="true">
          <rect width="24" height="24" rx="4" fill="var(--sun)"/>
          <path d="M8 5c-1.5 1-2.5 2.5-1.5 5s3.5 6 6 7.5 3.5.5 4.5-.8l-2.3-2.3-1.8 1c-1.2-.6-3.3-2.7-3.9-3.9l1-1.8L8 5z" fill="#fff"/>
        </svg>
        <span>555 01 87</span>
      </li>
      <li class="contact">
        <svg class="contact__icon" viewBox="0 0 24 24" aria-hidden="true">
          <rect width="24" height="24" rx="4" fill="var(--sun)"/>
          <rect x="5" y="7" width="14" height="10" rx="1" fill="#fff"/>
          <path d="M5.5 7.5 12 12.5l6.5-5" fill="none" stroke="var(--sun)" stroke-width="1.4"/>
        </svg>
        <span>hi@thornbeck.co</span>
      </li>
    </ul>
  </section>

</main>
</body>
</html>
```